professional coaching community needs new look for website

We require a website design that attracts professionals. We run a large, global professional coaching community (e.g. executive, business, personal coaches NOT sports coaches). Our members are committed to their professional and personal development and they enjoy building relationships with other coaches across the world. We also champion the success of coaches and the coaching industry by providing business support resources to our members. We do not mind which colours you use, but whatever the combination, the combinations must be professional and refined. It would be good to have some of the familiarity of the old site colours, with some new, more professional element. We have a number of requirements for the homepage and members design, and this is attached.

Reason: I am extending the deadline for this design, in order to give feedback and see how current designs can be tweaked.

Target Market(s)

Here are some ideas for images, which gives and idea of the target market also:

Ideas for website images:

1. http://www.pixelvault-example.com/stock-photo-48213907-business-success.php?st=3fa2816 (I like the people in this one – they seem very dynamic and a good mix of women and men)
2. http://www.pixelvault-example.com/stock-photo-51730284-business-communications.php?st=3fa2816 (I like all of the speech bubbles in this one, that’s what the Tandemora community does – pairs up in two’s or small groups and engages in professional talking)
3. http://www.pixelvault-example.com/stock-photo-37492618-global-business-working.php?st=3fa2816 (I like the combination of the world and the people talking in different groups)
4. http://www.pixelvault-example.com/stock-photo-46820375-global-business-people.php?st=b619204 (I like the world in this one – would be good to see combination of world and #1 dynamic people, which is the Tandemora community)

Industry/Entity Type

Building

Requirements
Must have
• See attached uploaded files including homepage design, member dashboard design, and example profile (profiles need to be included him banner design). Note that any text must not be build into graphic. It needs to be able to be edited via html.

```html
<!DOCTYPE html>
<html lang="en">
<head>
<meta charset="utf-8">
<title>Tandemora – Reciprocal peer coaching, mentoring and supervision</title>
<link rel="stylesheet" href="https://fonts.googleapis.com/css2?family=Roboto:wght@400;500;700&family=Ubuntu:wght@400;500&display=swap">
<style>
:root{
  --green-head:#84c789;
  --green-panel:#5da160;
  --green-link:#4e9a51;
  --navy:#1f4e8a;
  --navy-dark:#24497f;
  --orange:#f08a0c;
  --orange-light:#f9a72c;
  --grey-panel:#767676;
  --text:#444;
  --line:#e2e2e2;
  --footer:#3b3b3b;
}
*{box-sizing:border-box;margin:0;padding:0}
html,body{width:1006px;height:1200px;overflow:hidden;background:#fff}
body{font-family:"Ubuntu",sans-serif;color:var(--text);font-size:11px;position:relative}
.head-font{font-family:"Ubuntu",sans-serif;font-weight:400}

.site-header{position:absolute;left:0;top:0;width:1006px;height:118px;background:var(--green-head)}
.brand{position:absolute;left:100px;top:30px;display:flex;align-items:center;gap:8px}
.brand-mark{width:16px;height:16px;border-radius:50%;background:var(--navy)}
.brand-name{font-size:24px;color:#fff;font-weight:500}
.brand-tag{position:absolute;left:147px;top:69px;width:130px;font-family:"Roboto",sans-serif;font-size:9.5px;line-height:12px;color:var(--navy-dark);font-weight:500;text-align:right}
.lang{position:absolute;left:798px;top:14px;width:107px;height:24px;background:#fff;border:1px solid #ccc;border-radius:2px;font-family:"Roboto",sans-serif;font-size:9px;color:#555;display:flex;align-items:center;padding-left:8px;gap:6px}
.lang .flag{width:22px;height:12px;background:#26417a;border:1px solid #c22}
.lang .caret{margin-left:auto;margin-right:8px;width:0;height:0;border-left:5px solid transparent;border-right:5px solid transparent;border-top:5px solid #aaa}
.main-nav{position:absolute;left:346px;top:75px;display:flex}
.main-nav a{display:block;height:29px;line-height:29px;padding:0 10px;color:#fff;font-family:"Roboto",sans-serif;font-size:12px;text-decoration:none;letter-spacing:.2px}
.main-nav a.active{background:var(--navy-dark)}

.hero-band{position:absolute;left:0;top:118px;width:1006px;height:110px;background:linear-gradient(#fff,#ececec 40%,#fff)}
.tagline{position:absolute;left:100px;top:138px;font-size:23px;color:var(--navy)}
.btn-orange{display:inline-block;background:linear-gradient(var(--orange-light),var(--orange));color:#fff;font-size:14px;border-radius:2px;text-align:center;box-shadow:0 1px 2px rgba(0,0,0,.3)}
.quick-signup{position:absolute;left:330px;top:179px;width:130px;height:32px;line-height:32px}

.why-box{position:absolute;left:100px;top:226px;width:595px;height:204px;border:1px solid var(--line);background:linear-gradient(#fafafa,#fff);padding:16px 0 0 15px}
.why-box h2{font-size:21px;color:var(--navy);margin-bottom:6px}
.ticks{list-style:none}
.ticks li{position:relative;padding-left:20px;font-size:11px;line-height:23.5px}
.ticks li svg{position:absolute;left:0;top:7px}
.read-more{display:inline-block;margin-top:8px;color:var(--green-link);font-size:11.5px;text-decoration:underline}

.feature{position:absolute;left:100px;top:443px;width:595px;height:277px;border:4px solid #d5d5d5;background:linear-gradient(120deg,#3c4a5c,#dfe3e6 45%,#e8eaec 60%,#2a2a30)}
.feature-caption{position:absolute;left:0;right:0;bottom:0;height:109px;background:rgba(30,30,30,.55);text-align:center;color:#fff;padding-top:4px}
.feature-caption h3{font-size:27px;line-height:28px;font-weight:400}
.get-started{width:128px;height:32px;line-height:32px;margin-top:7px;font-size:15px}

.events{position:absolute;left:100px;top:733px;width:592px}
.section-title{font-size:20px;color:var(--navy)}
.events .rule{height:3px;background:var(--line);margin-top:7px}
.arrows{position:absolute;right:0;top:8px;display:flex;gap:10px}
.events h4{font-size:12.5px;color:var(--green-link);font-weight:500;margin-top:12px}
.events p{font-size:10.8px;line-height:17px;margin-top:3px;width:575px}
.events p a{color:var(--navy);font-style:italic;text-decoration:none}

.divider{position:absolute;left:100px;top:856px;width:805px;height:1px;background:var(--line)}

.welcome{position:absolute;left:100px;top:872px;width:510px}
.welcome .rule{width:325px;height:3px;background:var(--line);margin:8px 0 16px}
.welcome p{font-size:11px;line-height:19.3px;margin-bottom:8px}

.supporters{position:absolute;left:644px;top:872px;width:261px}
.supporters .rule{height:3px;background:var(--line);margin:8px 0 18px}
.logo-grid{display:grid;grid-template-columns:126px 126px;gap:9px;row-gap:10px}
.logo-tile{height:48px;border:1px solid #e2e2e2;background:#f5f5f5;display:flex;align-items:center;justify-content:center;gap:6px;font-size:16px;color:#666}
.logo-tile span.dot{width:12px;height:12px;border-radius:50%;background:#999}

.sidebar{position:absolute;left:704px;width:201px}
.login{top:128px;height:186px;background:var(--grey-panel);padding:11px 12px}
.panel-title{color:#fff;font-size:15px;margin-bottom:9px}
.field{height:24px;background:#fff;border:1px solid #a9d3ab;font-size:8.5px;color:#666;line-height:22px;padding-left:10px;margin-bottom:10px}
.login-row{display:flex;align-items:center;color:#fff;font-size:10.5px;gap:6px}
.box{width:11px;height:11px;background:#fff;border:1px solid #ccc}
.btn-green{margin-left:auto;background:var(--green-panel);color:#fff;font-size:10.5px;padding:0 10px;height:24px;line-height:24px}
.login-links{color:#fff;font-size:10.5px;line-height:19px;margin-top:10px;padding-left:2px}
.signup{top:321px;height:379px;background:var(--green-panel);padding:11px 12px}
.signup .ticks li{color:#fff;font-size:10.5px;line-height:15px;padding-left:22px;margin-bottom:8px}
.signup .ticks li svg{top:3px}
.signup .ticks{margin:2px 0 14px}
.signup .field{border-color:#ddd;margin-bottom:10px}
.terms{display:flex;gap:10px;color:#fff;font-size:10.5px;line-height:17px;margin-top:2px}
.terms .box{margin-top:3px;flex:none}
.btn-navy{display:block;margin:7px 0 0 auto;width:97px;height:23px;line-height:23px;text-align:center;background:var(--navy-dark);color:#fff;font-size:10.5px}
.focus-ad{top:708px;height:129px;background:linear-gradient(#5a8ccc,#9ec2e8 55%,#3d6fa8 80%,#c9c9c9);color:#fff;padding:6px 9px}
.focus-ad h3{font-size:19px;font-weight:400}
.focus-ad ul{list-style:none;font-size:7.5px;line-height:13px;margin-top:2px}

.site-footer{position:absolute;left:0;top:1108px;width:1006px;height:92px;background:var(--footer);color:#ddd;font-size:9.5px}
.copyright{position:absolute;left:100px;top:34px;line-height:19px}
.copyright span{color:#8dcc8f}
.social{position:absolute;right:101px;top:17px;text-align:right;font-size:10.5px}
.social-icons{display:flex;gap:9px;justify-content:flex-end;margin-top:10px}
.social-icons i{display:block;width:25px;height:25px;border-radius:3px}
</style>
</head>
<body>

<header class="site-header">
  <div class="brand"><span class="brand-mark"></span><span class="brand-name">Tandemora</span></div>
  <div class="brand-tag">Reciprocal peer coaching,<br>mentoring and supervision</div>
  <div class="lang"><span class="flag"></span>ENGLISH<span class="caret"></span></div>
  <nav class="main-nav">
    <a class="active" href="#">HOME</a><a href="#">COACHING</a><a href="#">MENTORING</a><a href="#">SUPERVISION</a><a href="#">RESOURCES</a><a href="#">JOIN US</a><a href="#">CONTACT US</a>
  </nav>
</header>

<div class="hero-band"></div>
<h1 class="tagline head-font">Join the most dynamic coaching community in the world</h1>
<a class="btn-orange quick-signup head-font">QUICK SIGNUP</a>

<section class="why-box">
  <h2 class="head-font">Why Choose Tandemorans?</h2>
  <ul class="ticks">
    <li><svg width="11" height="10"><path d="M1 5l3 3 6-7" stroke="#2d5d9a" stroke-width="2" fill="none"/></svg>Demonstrate integrity (coaching), competency (mentoring) and professionlism (supervision)</li>
    <li><svg width="11" height="10"><path d="M1 5l3 3 6-7" stroke="#2d5d9a" stroke-width="2" fill="none"/></svg>Be part of one of the most active coaching communities in the world</li>
    <li><svg width="11" height="10"><path d="M1 5l3 3 6-7" stroke="#2d5d9a" stroke-width="2" fill="none"/></svg>Be at your edge personally and professionally</li>
    <li><svg width="11" height="10"><path d="M1 5l3 3 6-7" stroke="#2d5d9a" stroke-width="2" fill="none"/></svg>Remove the isolation normally attached to working for yourself</li>
    <li><svg width="11" height="10"><path d="M1 5l3 3 6-7" stroke="#2d5d9a" stroke-width="2" fill="none"/></svg>All the known benefits of coaching, mentoring and supervision</li>
  </ul>
  <a class="read-more">READ MORE &gt;&gt;</a>
</section>

<section class="feature" role="img" aria-label="Photo of a businessman presenting a planning chart to two businesswomen">
  <div class="feature-caption">
    <h3 class="head-font">Personal &amp; Professional Development<br>for Coaches</h3>
    <a class="btn-orange get-started head-font">GET STARTED</a>
  </div>
</section>

<section class="events">
  <h2 class="section-title head-font">Upcoming Events</h2>
  <div class="arrows">
    <svg width="12" height="16"><path d="M10 1L3 8l7 7" stroke="#555" stroke-width="2" fill="none"/></svg>
    <svg width="12" height="16"><path d="M2 1l7 7-7 7" stroke="#555" stroke-width="2" fill="none"/></svg>
  </div>
  <div class="rule"></div>
  <h4>New rounds starting soon</h4>
  <p>Tandemora is an international community of coaches who engage in reciprocal coaching, mentoring and supervision for their own personal and professional development... <a>Read More</a></p>
</section>

<div class="divider"></div>

<section class="welcome">
  <h2 class="section-title head-font">Welcome to Our MainPage</h2>
  <div class="rule"></div>
  <p>Tandemora is an international community of coaches who engage in reciprocal coaching, mentoring and supervision for their own personal and professional development.</p>
  <p>By giving coaching and mentoring, Tandemorans receive coaching and mentoring, and by participating in supervision, Tandemorans give and receive through collaborative learning.</p>
  <p>Therefore, as a Tandemoran, you pay for your coaching, mentoring and supervision by giving it to another coach. As a result, because you're only paying us to orchestrate the reciprocal process, not for the coaching/mentoring/supervision itself, 8 sessions can cost much less than you'd normally pay for one session!</p>
</section>

<section class="supporters">
  <h2 class="section-title head-font">Thanks to our Supporters</h2>
  <div class="rule"></div>
  <div class="logo-grid">
    <div class="logo-tile">Coverwell</div>
    <div class="logo-tile">Regalbank</div>
    <div class="logo-tile"><span class="dot"></span>Northlight</div>
    <div class="logo-tile">Vantara</div>
    <div class="logo-tile"><span class="dot"></span>Brightside</div>
    <div class="logo-tile"><span class="dot"></span>Meridale</div>
  </div>
</section>

<aside class="sidebar login">
  <h3 class="panel-title head-font">MEMBER LOG IN</h3>
  <div class="field">USERNAME</div>
  <div class="field">PASSWORD</div>
  <div class="login-row"><span class="box"></span>Keep me logged in<span class="btn-green">LOG IN</span></div>
  <div class="login-links">Forgotten login?<br>Not a Tandemoran yet?</div>
</aside>

<aside class="sidebar signup">
  <h3 class="panel-title head-font">QUICK SIGN UP</h3>
  <ul class="ticks">
    <li><svg width="11" height="10"><path d="M1 5l3 3 6-7" stroke="#2d5d9a" stroke-width="2" fill="none"/></svg>Free to join</li>
    <li><svg width="11" height="10"><path d="M1 5l3 3 6-7" stroke="#2d5d9a" stroke-width="2" fill="none"/></svg>3 issues of Coaching<br>Research in Practice</li>
    <li><svg width="11" height="10"><path d="M1 5l3 3 6-7" stroke="#2d5d9a" stroke-width="2" fill="none"/></svg>Monthly issues of Lessons<br>from the Field</li>
    <li><svg width="11" height="10"><path d="M1 5l3 3 6-7" stroke="#2d5d9a" stroke-width="2" fill="none"/></svg>Access to our community</li>
    <li><svg width="11" height="10"><path d="M1 5l3 3 6-7" stroke="#2d5d9a" stroke-width="2" fill="none"/></svg>Online profile</li>
  </ul>
  <div class="field">FIRST NAME</div>
  <div class="field">LAST NAME</div>
  <div class="field">EMAIL ADDRESS</div>
  <div class="terms"><span class="box"></span><span>I have read the Tandemora terms and conditions.</span></div>
  <span class="btn-navy">SIGN UP NOW</span>
</aside>

<aside class="sidebar focus-ad" role="img" aria-label="Business team meeting at a table on a beach under a blue sky">
  <h3 class="head-font">Focusing on Change</h3>
  <ul><li>• Changing Behavior</li><li>• Driving Results</li><li>• Creating Sustainable Growth</li></ul>
</aside>

<footer class="site-footer">
  <div class="copyright">Copyright © 2009-2013 <span>Tandemora Pty Ltd.</span><br>All Right Reserved</div>
  <div class="social">Connect with our Community
    <div class="social-icons"><i style="background:#3b5a9a"></i><i style="background:#3fb3dc"></i><i style="background:#2a78b0"></i></div>
  </div>
</footer>

</body>
</html>
```